Book Cover Design

Design with title UNWAVERING
Subtitle: Ways to Kindle the Spark of Resolve
Author Name: Carla Jean Morrow
Put DAILY MERIDIAN BESTSELLER at top
Shimmer design, see inspirational images attached

```html
<!DOCTYPE html>
<html lang="en">
<head>
<meta charset="utf-8">
<title>Unwavering — Carla Jean Morrow</title>
<link rel="stylesheet" href="https://fonts.googleapis.com/css2?family=Cinzel:wght@400;500;600&family=Cormorant+SC:wght@500;600&display=swap">
<style>
  :root {
    --glow-white: #fffdf0;
    --glow-yellow: #fff3a8;
    --shimmer-cyan: #9fe3e6;
    --shimmer-teal: #7fc9c8;
    --shimmer-green: #c8e6a0;
    --shimmer-peach: #ffc9a0;
    --shimmer-pink: #f4a6d8;
    --shimmer-magenta: #e58fd6;
    --shimmer-violet: #a98de6;
    --shimmer-blue: #8fa8ee;
    --ink-plum: #5a1c3c;
    --ink-title: #ffffff;
  }
  * { margin: 0; padding: 0; box-sizing: border-box; }
  html, body {
    width: 800px;
    height: 1200px;
    overflow: hidden;
    background: #ffffff;
  }
  .cover {
    position: relative;
    width: 800px;
    height: 1200px;
    overflow: hidden;
    text-align: center;
  }
  .shimmer-field {
    position: absolute;
    inset: 0;
    background:
      radial-gradient(ellipse 260px 380px at 50% 10%, var(--glow-white) 0%, rgba(255,250,200,0.85) 35%, rgba(255,243,168,0) 75%),
      radial-gradient(ellipse 220px 700px at 22% 40%, rgba(255,255,255,0.55) 0%, rgba(255,255,255,0) 70%),
      radial-gradient(ellipse 220px 700px at 78% 40%, rgba(255,255,255,0.5) 0%, rgba(255,255,255,0) 70%),
      radial-gradient(ellipse 420px 360px at 55% 62%, rgba(244,166,216,0.95) 0%, rgba(244,166,216,0) 75%),
      radial-gradient(ellipse 360px 500px at 90% 30%, rgba(255,201,160,0.9) 0%, rgba(255,201,160,0) 75%),
      radial-gradient(ellipse 360px 520px at 8% 30%, rgba(159,227,230,0.95) 0%, rgba(159,227,230,0) 75%),
      radial-gradient(ellipse 300px 400px at 20% 55%, rgba(200,230,160,0.7) 0%, rgba(200,230,160,0) 75%),
      radial-gradient(ellipse 500px 420px at 30% 95%, rgba(143,168,238,0.95) 0%, rgba(143,168,238,0) 75%),
      radial-gradient(ellipse 500px 420px at 80% 95%, rgba(169,141,230,0.95) 0%, rgba(169,141,230,0) 75%),
      linear-gradient(90deg, var(--shimmer-teal) 0%, var(--shimmer-green) 25%, var(--shimmer-pink) 55%, var(--shimmer-magenta) 80%, var(--shimmer-peach) 100%);
  }
  .bestseller-line {
    position: absolute;
    top: 28px;
    left: 0;
    right: 0;
    font-family: "Cinzel", serif;
    font-weight: 500;
    font-size: 28px;
    letter-spacing: 1px;
    color: var(--ink-title);
    text-shadow: 0 0 6px rgba(120,90,40,0.35);
  }
  .author-name {
    position: absolute;
    top: 84px;
    left: 0;
    right: 0;
    font-family: "Cinzel", serif;
    font-weight: 500;
    font-size: 40px;
    letter-spacing: 3px;
    color: var(--ink-plum);
  }
  .book-title {
    position: absolute;
    top: 570px;
    left: 0;
    right: 0;
    font-family: "Cinzel", serif;
    font-weight: 400;
    font-size: 104px;
    letter-spacing: 2px;
    color: var(--ink-title);
    text-shadow: 0 2px 6px rgba(90,40,110,0.45), 0 0 2px rgba(90,40,110,0.35);
  }
  .book-subtitle {
    position: absolute;
    top: 830px;
    left: 0;
    right: 0;
    font-family: "Cormorant SC", "Cinzel", serif;
    font-weight: 600;
    font-size: 56px;
    line-height: 68px;
    color: var(--ink-plum);
  }
</style>
</head>
<body>
  <main class="cover">
    <div class="shimmer-field" role="img" aria-label="Shimmering pastel rainbow texture with soft beams of light glowing from the top"></div>
    <p class="bestseller-line">DAILY MERIDIAN BESTSELLER</p>
    <p class="author-name">CARLA JEAN MORROW</p>
    <h1 class="book-title">UNWAVERING</h1>
    <h2 class="book-subtitle">Ways to Kindle<br>the Spark<br>of Resolve</h2>
  </main>
</body>
</html>
```